Brisko Sky Park needs a new upscale business card design for our high end aircraft hangar complex

Brisko Sky Park (BSP) is a large, upscale jet hangar complex in the US housing expensive aircraft. We need a new business card design, using our current logo. We will be attending a industry convention and need a card design that will stand out and be remembered by aircraft owners and private pilots.

Target Market(s)

Aircraft pilots or owners looking for a new upscale hangar

Industry/Entity Type

Airport

Contact Information for Business Card

I like to use very heavy card stock, 400#, double sided. Square, no rounded edges please.

Colors
3276b5
0255a3
85abd2

Requirements
Must have
• An expensive, classy design, vivid colors.
Nice to have
• Needs to look very expensive and classy, and have some "pop". Designer must be able to download or copy my current typeface or fonts.
• One card side might be black with the "Logo and Brisko Sky Park Double line image in blue (or try gold, or glossy black), and perhaps have a grayed out "K480 jet silhouette". The other card side would have our contact info, and perhaps the "BSP Logo only". I'd like my contact info 'stacked', not in a paragraph format.
Should not have
• Should not look "too busy". Having a double-sided card will help.

```html
<!DOCTYPE html>
<html lang="en">
<head>
<meta charset="utf-8">
<title>Brisko Sky Park – Business Card</title>
<link href="https://fonts.googleapis.com/css2?family=Open+Sans:wght@400;600&display=swap" rel="stylesheet">
<style>
  :root {
    --backdrop: #8f8f8f;
    --card: #0b0b0c;
    --brand-blue: #3276b5;
    --band-blue: #37609a;
    --light-blue: #85abd2;
    --ink: #f1f1f1;
    --muted: #b9b9b9;
    --ghost: #202124;
  }
  * { margin: 0; padding: 0; box-sizing: border-box; }
  html, body {
    width: 1200px; height: 844px; overflow: hidden;
    background: var(--backdrop);
    font-family: "Open Sans", Arial, sans-serif;
  }
  .canvas {
    position: relative; width: 1200px; height: 844px;
    display: flex; align-items: center; justify-content: center; gap: 40px;
  }
  .card {
    position: relative; width: 530px; height: 303px;
    background: var(--card);
    box-shadow: 0 10px 28px rgba(0,0,0,.35);
    overflow: hidden;
  }
  /* Contact side */
  .accent-area {
    position: absolute; right: 0; top: 0; width: 470px; height: 152px;
    background: linear-gradient(100deg, var(--card) 0%, var(--band-blue) 55%, var(--band-blue) 100%);
  }
  .contact { position: absolute; left: 28px; top: 132px; color: var(--ink); }
  .contact__name {
    color: var(--brand-blue); font-size: 15px; font-weight: 400;
    letter-spacing: .02em; text-transform: uppercase;
  }
  .contact__title { color: var(--muted); font-size: 11px; margin-bottom: 8px; }
  .contact__list { list-style: none; }
  .contact__list li {
    display: flex; align-items: center; gap: 8px;
    font-size: 11.5px; line-height: 17px; white-space: nowrap;
  }
  .contact__list--online { position: absolute; left: 112px; top: 92px; }
  .icon { width: 11px; height: 11px; flex: none; fill: var(--light-blue); }
  /* Brand side */
  .aircraft-area {
    position: absolute; left: 0; top: 0; width: 62%; height: 100%;
    background: radial-gradient(ellipse at 40% 45%, var(--ghost) 0%, var(--card) 70%);
  }
  .brand {
    position: absolute; right: 36px; top: 112px; text-align: right;
    color: var(--brand-blue); font-weight: 600;
  }
  .brand__initials { font-size: 52px; line-height: 1; letter-spacing: .06em; }
  .brand__name { font-size: 15px; letter-spacing: .18em; text-transform: uppercase; margin-top: 4px; }
</style>
</head>
<body>
<main class="canvas">

  <section class="card card--contact" aria-label="Contact side">
    <div class="accent-area" role="img" aria-label="Decorative blue wing-style bands"></div>

    <div class="contact">
      <h1 class="contact__name">Alden Marsh</h1>
      <p class="contact__title">CEO/Founder</p>
      <ul class="contact__list">
        <li><svg class="icon" viewBox="0 0 12 12"><path d="M2.5 1l2 2.2-1 1.3a7 7 0 0 0 4 4l1.3-1 2.2 2-1.4 1.5C5 10.5 1.5 7 1 2.4z"/></svg>614 502 7381</li>
        <li><svg class="icon" viewBox="0 0 12 12"><path d="M3 0h6v12H3zM4 1.5v8h4v-8z"/></svg>614 502 7382</li>
        <li><svg class="icon" viewBox="0 0 12 12"><path d="M3 1h6v3h2v6H1V4h2zm1 1v3h4V2zM3 7v1h6V7z"/></svg>614 502 7390</li>
      </ul>
      <ul class="contact__list contact__list--online">
        <li><svg class="icon" viewBox="0 0 12 12"><path d="M0 2h12v8H0zm1 1v.4l5 3.3 5-3.3V3z"/></svg>hello@briskoskypark.com</li>
        <li><svg class="icon" viewBox="0 0 12 12"><circle cx="6" cy="6" r="5.5"/></svg>www.briskoskypark.com</li>
        <li><svg class="icon" viewBox="0 0 12 12"><path d="M6 0a4 4 0 0 0-4 4c0 3 4 8 4 8s4-5 4-8a4 4 0 0 0-4-4zm0 2.3a1.7 1.7 0 1 1 0 3.4 1.7 1.7 0 0 1 0-3.4z"/></svg>2140 Ridgefield Way, Anchorage, Alaska 99502</li>
      </ul>
    </div>
  </section>

  <section class="card card--brand" aria-label="Brand side">
    <div class="aircraft-area" role="img" aria-label="Faint grey silhouette of a K480 business jet"></div>
    <div class="brand">
      <p class="brand__initials">BSP</p>
      <p class="brand__name">Brisko Sky Park</p>
    </div>
  </section>

</main>
</body>
</html>
```